Contemporary new French wine brand needs logo and series of label design

to design a new contemporary logo and series of labels for a new French wine brand. We hope to attract not just current French wine drinkers but new ones who may appreciate a less traditional and more modern style.
Updates

Reason: we are wanting to extend the project for a few days more to receive more submissions since we had fewer designs submitted than we were expecting, maybe because of the holidays.

Target Market(s)

people who follow the arts community (eg. music, theatre, visual/video arts, dance) --- all mature ages.

Industry/Entity Type

French Wine

Requirements
Must have
• a clear, memorable treatment for the name CLAVINE with accompanying logo.
Nice to have
• embossing, matte/gloss refinement, tasteful foil stamping, coated stock for the whites to help the integrity of the paper in and out of ice buckets. A combo of say, three types of fonts; a semi custom font for the brand name Clavine and maybe a script and one other.
Should not have
• not traditional French

```html
<!DOCTYPE html>
<html lang="en">
<head>
<meta charset="utf-8">
<title>Clavine — Sauvignon Blanc label</title>
<link rel="stylesheet" href="https://fonts.googleapis.com/css2?family=Montserrat:wght@600;700&family=Playfair+Display:ital@1&display=swap">
<style>
  :root {
    --label-black: #050505;
    --band-tone: #111111;
    --band-edge: #0a0a0a;
    --giant-letter: #262626;
    --wordmark-white: #ffffff;
    --varietal-grey: #b9b9b9;
  }
  html, body {
    margin: 0;
    padding: 0;
    overflow: hidden;
    background: var(--label-black);
  }
  .label {
    position: relative;
    width: 1049px;
    height: 1200px;
    overflow: hidden;
    background: var(--label-black);
  }
  .wave-band {
    position: absolute;
    left: 0;
    width: 100%;
    background: linear-gradient(180deg, var(--band-edge) 0%, var(--band-tone) 50%, var(--band-edge) 100%);
  }
  .wave-band--top { top: 0; height: 435px; }
  .wave-band--bottom { top: 724px; height: 476px; }
  .giant-letters {
    position: absolute;
    margin: 0;
    font-family: "Montserrat", sans-serif;
    font-weight: 700;
    font-size: 370px;
    line-height: 1;
    letter-spacing: 0.12em;
    white-space: nowrap;
    color: var(--giant-letter);
    opacity: 0.9;
  }
  .giant-letters--top { top: 68px; left: -210px; }
  .giant-letters--bottom { top: 761px; left: -120px; }
  .title-block {
    position: absolute;
    top: 510px;
    left: 0;
    width: 100%;
    text-align: center;
  }
  .wordmark {
    margin: 0;
    font-family: "Montserrat", sans-serif;
    font-weight: 600;
    font-size: 92px;
    line-height: 1;
    letter-spacing: 0.22em;
    padding-left: 0.22em;
    color: var(--wordmark-white);
  }
  .varietal {
    margin: 50px 0 0;
    font-family: "Playfair Display", serif;
    font-style: italic;
    font-size: 28px;
    letter-spacing: 0.14em;
    color: var(--varietal-grey);
  }
</style>
</head>
<body>
  <main class="label">
    <div class="wave-band wave-band--top" role="img" aria-label="Band of fine horizontal wavy lines"></div>
    <div class="wave-band wave-band--bottom" role="img" aria-label="Band of fine horizontal wavy lines"></div>

    <p class="giant-letters giant-letters--top" aria-hidden="true">VINE</p>
    <p class="giant-letters giant-letters--bottom" aria-hidden="true">CLAV</p>

    <header class="title-block">
      <h1 class="wordmark">CLAVINE</h1>
      <p class="varietal">Sauvignon Blanc</p>
    </header>
  </main>
</body>
</html>
```